Web Header needed for an inspirational coaching company's website - ongoing work

We need a beautifully designed web header to replace my current one at my homepage on my website www.kelvoria.com
There will be continuous work required for various creative work in the future if your work is selected.
I work with corporate professionals and executives to bring clarity and joy back to their career. It needs to be elegant, sophisticated, intelligent, but friendly and inspiring at the same time.
Thank you!
Target Market(s)
Corporate profesionals and executives
Industry/Entity Type
It Company
Colors
Designer to choose colors to be used in the design.
Look and feel

```html
<!DOCTYPE html>
<html lang="en">
<head>
<meta charset="utf-8">
<title>Kelvoria – Your Career Partner</title>
<link rel="stylesheet" href="https://fonts.googleapis.com/css2?family=Arimo:wght@400;700&family=Bebas+Neue&family=Cormorant+Garamond:wght@600&family=Lexend:wght@500&family=Raleway:wght@400;600;700&display=swap">
<style>
:root{
  --teal:#1e8c82;
  --ink:#3f3f3f;
  --muted:#555;
  --white:#fff;
  --band:#9a9a9a;
  --sky-top:#5f93ad;
  --sky-mid:#7fb0c4;
  --city:#2f6f8f;
  --orange:#f0561e;
  --paper:#ffffff;
}
*{margin:0;padding:0;box-sizing:border-box}
html,body{width:1095px;height:1200px;overflow:hidden;background:var(--paper)}
body{position:relative;font-family:"Raleway",sans-serif;color:var(--ink)}
.hero{position:absolute;left:0;top:0;width:1095px;height:396px;
  background:linear-gradient(180deg,var(--sky-top) 0%,var(--sky-mid) 45%,var(--city) 100%)}
.hero-portrait{position:absolute;left:700px;top:76px;width:255px;height:320px;
  background:linear-gradient(180deg,#2a2326 0%,#3b2e2e 55%,var(--orange) 85%,#e24e18 100%);
  border-radius:120px 120px 0 0}
.band{position:absolute;left:0;top:396px;width:1095px;height:13px;background:var(--band)}
.brand{position:absolute;left:20px;top:24px;font-family:"Arimo",sans-serif;font-weight:700;font-size:17px;letter-spacing:2px;color:var(--white);display:flex;align-items:center;gap:7px}
.brand i{display:block;width:9px;height:9px;border-radius:50%;background:var(--orange)}
.nav{position:absolute;top:29px;left:0;width:1095px;font-family:"Arimo",sans-serif;font-weight:700;font-size:10.5px;color:var(--white)}
.nav a{position:absolute;color:inherit;text-decoration:none;white-space:nowrap}
.nav .contact{top:-12px;left:933px;width:90px;height:35px;border:2px solid var(--white);border-radius:18px;text-align:center;line-height:31px;font-size:11px;font-weight:400}
.headline{position:absolute;left:194px;top:124px;font-family:"Bebas Neue",sans-serif;font-size:66px;line-height:1;color:var(--white);letter-spacing:-0.5px}
.tagline{position:absolute;left:275px;top:189px;font-family:"Lexend",sans-serif;font-weight:500;font-size:21px;letter-spacing:-0.8px;color:#1c1c1c}
.welcome{position:absolute;left:0;width:1095px;top:468px;text-align:center;font-family:"Cormorant Garamond",serif;font-weight:600;font-size:24px;letter-spacing:1px;color:var(--teal)}
.lede{position:absolute;left:0;width:1095px;top:510px;text-align:center;font-weight:700;font-size:12px;color:var(--muted)}
.clients{position:absolute;left:165px;top:555px;width:768px;height:52px;display:flex;align-items:center;justify-content:space-between;font-family:"Raleway",sans-serif;font-weight:700;font-size:14px;color:#444}
.clients span{display:flex;align-items:center;gap:5px}
.clients i{display:block;width:10px;height:10px;background:#444}
.quote{position:absolute;left:0;width:1095px;top:634px;text-align:center;font-family:"Cormorant Garamond",serif;font-weight:600;font-size:23px;letter-spacing:1px;color:var(--teal)}
.story{position:absolute;left:160px;top:688px;width:380px;font-size:12.3px;line-height:19.5px;color:#4a4a4a}
.story p{margin-bottom:13px}
.story a{color:var(--teal);text-decoration:none}
.story .testimonial{font-weight:700;color:#333}
.speaker-photo{position:absolute;left:636px;top:690px;width:226px;height:239px;
  background:linear-gradient(180deg,#dfe8f6 0%,#c9d8ee 45%,var(--orange) 75%,#ee5a22 100%)}
.caption{position:absolute;left:636px;top:956px;width:230px;font-size:10.5px;line-height:14px;color:#555}
.tile{position:absolute;top:1061px;width:240px;height:139px}
.tile.checklist{left:160px;background:linear-gradient(160deg,#f4f4f4,#d8d8d8)}
.tile.workshop{left:427px;background:linear-gradient(180deg,#e9e6e4 0%,#c7413a 45%,#efefef 100%)}
.tile.vision{left:695px;background:linear-gradient(180deg,#4e8fa0 0%,#8fb6a6 55%,#c79b52 100%)}
</style>
</head>
<body>
<header class="hero" role="img" aria-label="City skyline at dusk under a blue sky">
</header>
<div class="hero-portrait" role="img" aria-label="Portrait of the coach in an orange top"></div>
<div class="band"></div>

<div class="brand"><i></i>KELVORIA</div>
<nav class="nav">
  <a style="left:281px">Home</a>
  <a style="left:335px">About Lian Wen</a>
  <a style="left:433px">Testimonial</a>
  <a style="left:514px">Methodology</a>
  <a style="left:606px">Coaching &amp; Mentoring</a>
  <a style="left:740px">Workshop</a>
  <a style="left:816px">Corporate</a>
  <a style="left:888px">Blog</a>
  <a class="contact">CONTACT</a>
</nav>

<h1 class="headline">YOUR CAREER PARTNER</h1>
<p class="tagline">Bring Clarity to Your Career</p>

<h2 class="welcome">Welcome to Discover Your Kelvoria</h2>
<p class="lede">A place for professionals &amp; executives to find clarity in their career</p>

<div class="clients">
  <span><i></i>Arvenco</span>
  <span>Talwyn</span>
  <span>Hexpoint</span>
  <span>Lumora</span>
  <span>Marcelle</span>
  <span>Ibrex</span>
  <span>Dorran</span>
  <span>Tixora</span>
  <span>Norbank</span>
</div>

<h2 class="quote">"Best program I have ever attended in my career - Marisa"</h2>

<section class="story">
  <p>Welcome! I am Lian Wen, I am known for helping professionals and executives find clarity in their career and life, so they can focus on what really matters and succeed with joy and meaning.</p>
  <p>In 2008, I was a senior executive with a young family seemingly had it all. However, I felt tired, unhappy and wanted to quit. At the end, I didn't quit, instead I began a search for an answer.</p>
  <p>I did extensive research over the years. What I found is that what I felt is normal and can be turned around with a simple approach.</p>
  <p>The approach gave me the direction, energy, made me a better leader and mum, and took me to a whole new level of joy, success, and career fulfilment. My greatest joy today is enabling others to do the same. <a>Read my search and journey.</a></p>
  <p class="testimonial">"I know Lian Wen is the best person to guide me on this journey. Lian Wen makes you feel comfortable while pushing you to be your best - Tomas, Director of Sales &amp; Alliances"</p>
</section>

<div class="speaker-photo" role="img" aria-label="The coach speaking at a seminar with a headset microphone"></div>
<p class="caption">Lian Wen Hsu. Executive Coach. Fortune 100 Exec. Strength Psychology Expert. Mother.</p>

<div class="tile checklist" role="img" aria-label="Hand ticking boxes on a checklist"></div>
<div class="tile workshop" role="img" aria-label="Workshop group in a meeting room with a whiteboard"></div>
<div class="tile vision" role="img" aria-label="Hands framing a view of a golden field under a blue sky"></div>
</body>
</html>
```